Offshore Energy Projects Management Consultancy needs a business card design

Logo available. We provide teams to deliver engineering consultancy, project management and delivery teams mainly in the offshore renewables sector. The company is all about bringing the right people to a project to deliver the scope.

The business card will be used for all staff.

The business card should be quite simple, vibrant and uncluttered but convey experience, enthusiasm and integration.

Target Market(s)

Energy Project Developers and Tier 1 construction companies

Contact Information for Business Card

Logo should be on the back of the card. I'm happy for the designer to play with the colour of the logo and background colour.

Front of the card should convey all the must have information in a clear and professional manner but without being overly traditional.

Colors

Designer to choose colors to be used in the design.

Requirements
Must have
• Land Line Tel Number, Mobile Tel Number, Email, business address, web address.

```html
<!DOCTYPE html>
<html lang="en">
<head>
<meta charset="utf-8">
<title>Tidewater Delivery Group – Business Card</title>
<link href="https://fonts.googleapis.com/css2?family=PT+Serif:wght@400;700&display=swap" rel="stylesheet">
<style>
  :root {
    --backdrop: #2b2b2d;
    --card-white: #ffffff;
    --brand-blue: #1f73c4;
    --brand-sky: #2aa3df;
    --band-blue: #1e8fd8;
    --ink-grey: #6b6b6b;
    --rule-grey: #9a9a9a;
    --shadow: rgba(0,0,0,0.45);
  }
  * { box-sizing: border-box; margin: 0; padding: 0; }
  html, body {
    width: 1200px; height: 1000px; overflow: hidden;
    background: var(--backdrop);
    font-family: "PT Serif", Georgia, serif;
  }
  .canvas { position: relative; width: 1200px; height: 1000px; }

  .card {
    position: absolute; left: 250px; width: 700px; height: 400px;
    box-shadow: 0 12px 30px var(--shadow);
    overflow: hidden;
  }

  /* Front */
  .card--front { top: 70px; background: var(--card-white); }
  .card--front .bottom-band {
    position: absolute; left: 0; right: 0; bottom: 0; height: 14px;
    background: var(--band-blue);
  }
  .front-logo {
    position: absolute; left: 40px; top: 170px; width: 270px;
    display: flex; align-items: center; gap: 12px;
  }
  .front-logo .mark-dot {
    width: 26px; height: 26px; border-radius: 50%;
    background: var(--brand-blue); flex: none;
  }
  .front-logo .company-name {
    color: var(--brand-blue); font-weight: 700; font-size: 22px;
    letter-spacing: 1px; line-height: 1.15; text-transform: uppercase;
  }
  .divider {
    position: absolute; left: 360px; top: 60px; width: 1px; height: 220px;
    background: var(--rule-grey);
  }
  .contact {
    position: absolute; left: 400px; top: 48px; width: 270px;
    color: var(--ink-grey);
  }
  .contact .person-name {
    color: var(--brand-blue); font-size: 30px; font-weight: 400;
    letter-spacing: 1px; text-transform: uppercase; line-height: 1;
  }
  .contact .job-title {
    font-size: 17px; letter-spacing: 1px; text-transform: uppercase;
    margin-top: 4px;
  }
  .contact .address {
    font-size: 15px; line-height: 1.35; margin-top: 16px; padding-left: 40px;
  }
  .contact .lines { list-style: none; margin-top: 18px; font-size: 14px; }
  .contact .lines li { display: flex; align-items: center; gap: 10px; height: 22px; }
  .contact .lines svg { width: 14px; height: 14px; fill: var(--brand-sky); flex: none; }
  .front-web {
    position: absolute; right: 60px; bottom: 50px;
    color: var(--brand-blue); font-size: 17px;
  }

  /* Back */
  .card--back {
    top: 530px;
    background: linear-gradient(160deg, var(--brand-sky) 0%, var(--brand-blue) 100%);
    color: var(--card-white);
  }
  .back-logo {
    position: absolute; left: 0; right: 0; top: 130px;
    display: flex; justify-content: center; align-items: center; gap: 18px;
  }
  .back-logo .mark-dot {
    width: 44px; height: 44px; border-radius: 50%;
    background: var(--card-white);
  }
  .back-logo .company-name {
    font-weight: 700; font-size: 40px; letter-spacing: 2px;
    text-transform: uppercase; line-height: 1.1;
  }
  .back-web {
    position: absolute; left: 0; right: 0; top: 300px; text-align: center;
    font-size: 18px;
  }
</style>
</head>
<body>
<div class="canvas">

  <section class="card card--front">
    <div class="front-logo">
      <span class="mark-dot"></span>
      <span class="company-name">Tidewater<br>Delivery Group</span>
    </div>
    <div class="divider"></div>
    <div class="contact">
      <h1 class="person-name">Daniel Marsh</h1>
      <p class="job-title">Casting Manager</p>
      <p class="address">48 Harbour Lane<br>Northport 2210</p>
      <ul class="lines">
        <li><svg viewBox="0 0 24 24"><path d="M6.6 10.8a15.2 15.2 0 0 0 6.6 6.6l2.2-2.2a1 1 0 0 1 1-.25 11.4 11.4 0 0 0 3.6.57 1 1 0 0 1 1 1V20a1 1 0 0 1-1 1A17 17 0 0 1 3 4a1 1 0 0 1 1-1h3.5a1 1 0 0 1 1 1c0 1.25.2 2.45.57 3.57a1 1 0 0 1-.25 1z"/></svg>1234567890</li>
        <li><svg viewBox="0 0 24 24"><path d="M7 1h10a2 2 0 0 1 2 2v18a2 2 0 0 1-2 2H7a2 2 0 0 1-2-2V3a2 2 0 0 1 2-2zm0 3v14h10V4zm5 15.5a1.2 1.2 0 1 0 0 2.4 1.2 1.2 0 0 0 0-2.4z"/></svg>1234567890</li>
        <li><svg viewBox="0 0 24 24"><path d="M2 5h20v14H2zm2 2v.4l8 5 8-5V7zm0 2.8V17h16V9.8l-8 5z"/></svg>name@mail.com</li>
      </ul>
    </div>
    <p class="front-web">www.website.com</p>
    <div class="bottom-band"></div>
  </section>

  <section class="card card--back">
    <div class="back-logo">
      <span class="mark-dot"></span>
      <span class="company-name">Tidewater<br>Delivery Group</span>
    </div>
    <p class="back-web">www.website.com</p>
  </section>

</div>
</body>
</html>
```